New Locksmith Business needs a newspaper ad

We need an ad for a new locksmith business in Colorado called Riverbend Key Co. Our service area is located near several world-class ski resorts, which fuel the local economy. We are a comprehensive locksmith business offering automotive, commercial and residential services. We provide modern, tech-savvy digital security solutions for your home or business.

Size of ad: 3.22" x 3.44" | PDF needed for final artwork file

Target Market(s)

Local residents, businesses, hotels and resorts. As well as visitors to the area that may need emergency lock out services. High income, high net worth clients.

Industry/Entity Type

Locksmith

Font styles to use
Sans Serif

Requirements
Must have
• *Include: Logo
*Include: 970.318.2957
*Include: riverbendkeyco.example
*Include photo of Gus, he's the locksmith
*Include text: New Business!
*Include text: Auto | Residential | Commercial
*Include: Innovative Locksmith Solutions
*Colors from the logo are the main colors to use; accent color is Chrome Yellow (#ffac00)
*Bank Gothic is the headline font and we like to use Oswald font for all other text
Nice to have
• It would be nice to include another photo, in addition to the photo of Gus, if there is space. I know it is a small space, so no worries if adding another photo will not work.

```html
<!DOCTYPE html>
<html lang="en">
<head>
<meta charset="utf-8">
<title>Riverbend Key Co – Newspaper Ad</title>
<link href="https://fonts.googleapis.com/css2?family=Michroma&family=Oswald:wght@400;500;600&display=swap" rel="stylesheet">
<style>
  :root {
    --brand-blue: #1b6fc4;
    --band-gray: #6b6c70;
    --tag-gray: #5f6064;
    --chrome-yellow: #ffac00;
    --paper: #ffffff;
    --stage: #e8ebee;
    --photo-skin: #b98a6a;
    --photo-shirt: #2f4fb0;
    --photo-door: #7a5232;
    --photo-glow: #d9c98a;
  }
  * { margin: 0; padding: 0; box-sizing: border-box; }
  html, body { width: 1200px; height: 945px; overflow: hidden; background: var(--stage); }
  .ad {
    position: absolute; left: 200px; top: 45px;
    width: 800px; height: 855px; background: var(--paper);
    font-family: "Oswald", sans-serif;
    box-shadow: 0 4px 18px rgba(0,0,0,.12);
  }
  .ad__top { position: absolute; left: 0; top: 0; width: 800px; height: 388px; display: flex; }
  .locksmith-photo {
    width: 341px; height: 388px;
    background: linear-gradient(160deg, var(--photo-door) 0%, var(--photo-skin) 42%, var(--photo-shirt) 78%, var(--photo-shirt) 100%);
  }
  .brand-panel { position: relative; flex: 1; height: 388px; background: var(--paper); }
  .brand-panel svg { position: absolute; inset: 0; }
  .headline-band { position: absolute; left: 0; top: 388px; width: 800px; height: 208px; background: var(--band-gray); }
  .headline-band svg { display: block; }
  .ad__bottom { position: absolute; left: 0; top: 596px; width: 800px; height: 259px; display: flex; }
  .contact-panel { width: 377px; height: 259px; background: var(--brand-blue); }
  .contact-panel svg { display: block; }
  .smart-lock-photo {
    flex: 1; height: 259px;
    background: linear-gradient(90deg, var(--photo-glow) 0%, #c9a877 22%, var(--photo-door) 30%, #8a5e3a 70%, #6a4428 100%);
  }
  .t-head { font-family: "Michroma", sans-serif; }
  .t-body { font-family: "Oswald", sans-serif; }
</style>
</head>
<body>
  <main class="ad">
    <section class="ad__top">
      <div class="locksmith-photo" role="img" aria-label="Photo of Gus the locksmith smiling in a blue polo shirt in front of a wooden door"></div>
      <div class="brand-panel">
        <svg width="459" height="388" viewBox="0 0 459 388">
          <g class="new-business-tag">
            <path d="M99 0 H354 V62 L346 68 L338 62 L330 68 L322 62 L314 68 L306 62 L298 68 L290 62 L282 68 L274 62 L266 68 L258 62 L250 68 L242 62 L234 68 L226 62 L218 68 L210 62 L202 68 L194 62 L186 68 L178 62 L170 68 L162 62 L154 68 L146 62 L138 68 L130 62 L122 68 L114 62 L106 68 L99 62 Z" fill="var(--tag-gray)"/>
            <text class="t-body" x="226" y="46" text-anchor="middle" font-size="34" font-weight="500" fill="#fff" textLength="220" lengthAdjust="spacingAndGlyphs">NEW BUSINESS!</text>
          </g>
          <g class="brand-mark">
            <circle cx="230" cy="215" r="46" fill="var(--brand-blue)"/>
            <text class="t-head" x="230" y="345" text-anchor="middle" font-size="38" fill="var(--brand-blue)" textLength="390" lengthAdjust="spacingAndGlyphs">RIVERBEND KEY CO</text>
          </g>
        </svg>
      </div>
    </section>

    <section class="headline-band">
      <svg width="800" height="208" viewBox="0 0 800 208">
        <text class="t-head" x="47" y="90" font-size="76" fill="#fff" textLength="702" lengthAdjust="spacingAndGlyphs">INNOVATIVE</text>
        <text class="t-head" x="47" y="132" font-size="36" fill="var(--chrome-yellow)" textLength="702" lengthAdjust="spacingAndGlyphs">LOCKSMITH SOLUTIONS</text>
        <text class="t-body" x="50" y="183" font-size="38" font-weight="500" fill="#fff" letter-spacing="5">
          <tspan>AUTO</tspan><tspan fill="var(--chrome-yellow)" dx="10">|</tspan><tspan dx="10">RESIDENTIAL</tspan><tspan fill="var(--chrome-yellow)" dx="10">|</tspan><tspan dx="10">COMMERCIAL</tspan>
        </text>
      </svg>
    </section>

    <section class="ad__bottom">
      <div class="contact-panel">
        <svg width="377" height="259" viewBox="0 0 377 259">
          <text class="t-body" x="50" y="138" font-size="58" font-weight="500" fill="#fff" textLength="290" lengthAdjust="spacingAndGlyphs">970.318.2957</text>
          <text class="t-body" x="50" y="171" font-size="28" font-weight="500" fill="#fff" textLength="290" lengthAdjust="spacingAndGlyphs">RIVERBENDKEYCO.EXAMPLE</text>
        </svg>
      </div>
      <div class="smart-lock-photo" role="img" aria-label="Photo of a hand holding a smartphone with a lock app next to a smart door lock on a wooden door"></div>
    </section>
  </main>
</body>
</html>
```